Geschäftspapiere für Unternehmensberatung
Zielgruppe
Unternehmensberatung,
Vorstände, Geschäftsführer, Personalleiter, Führungskräfte
Aufgabenstellung
Das Briefpapier muss veränderbar sein, da die Daten sich noch ändern werden. Diese liegen aber erst nach der Ummeldung im Handelsregister endgültig vor.
Eine Vorlage unseres alten Briefpapiers folgt.

```html
<!DOCTYPE html>
<html lang="de">
<head>
<meta charset="utf-8">
<title>Nordhafen Beratungshaus – Briefbogen</title>
<link href="https://fonts.googleapis.com/css2?family=Open+Sans:wght@400;600;700&display=swap" rel="stylesheet">
<style>
  :root {
    --bg: #dcdadd;
    --paper: #ffffff;
    --band-grey: #f1f1f1;
    --brand-blue: #3f55a2;
    --ink: #1a1a1a;
    --rule: #6a6a6a;
  }
  * { margin: 0; padding: 0; box-sizing: border-box; }
  html, body { width: 1200px; height: 1200px; overflow: hidden; }
  body { background: var(--bg); font-family: "Open Sans", sans-serif; color: var(--ink); position: relative; }

  .letterhead {
    position: absolute; left: 302px; top: 179px; width: 595px; height: 841px;
    background: var(--paper); box-shadow: 2px 3px 6px rgba(0,0,0,.18);
  }
  .header-band { position: absolute; left: 0; top: 0; width: 100%; height: 116px; background: var(--band-grey); }
  .brand-name {
    position: absolute; right: 30px; top: 44px; display: flex; align-items: center; gap: 8px;
    font-size: 15px; font-weight: 600; letter-spacing: .06em; color: var(--brand-blue);
  }
  .brand-dot { width: 11px; height: 11px; border-radius: 50%; background: var(--brand-blue); }

  .sender-line { position: absolute; left: 68px; top: 140px; font-size: 5.6px; color: var(--ink); white-space: nowrap; }
  .sender-line .accent { color: var(--brand-blue); font-weight: 700; }
  .sender-line .strong { font-weight: 700; }

  .reference-block {
    position: absolute; left: 354px; top: 142px; height: 144px; border-left: 1px solid var(--rule);
    padding-left: 9px; padding-top: 2px;
    font-size: 8px; font-weight: 600; color: var(--brand-blue); line-height: 12px;
  }
  .reference-block .gap { height: 12px; }

  .fold-mark { position: absolute; left: 0; width: 20px; height: 1px; }
  .fold-mark--upper { top: 297px; background: var(--brand-blue); }
  .fold-mark--lower { top: 420px; background: var(--ink); }

  .footer-band { position: absolute; left: 0; top: 690px; width: 100%; height: 109px; background: var(--band-grey); }
  .footer-col {
    position: absolute; top: 14px; height: 82px; border-left: 1px solid var(--rule); padding-left: 9px;
    font-size: 6.6px; line-height: 9px; white-space: nowrap;
  }
  .footer-col h4 { font-size: 6.6px; font-weight: 700; color: var(--brand-blue); margin-bottom: 9px; line-height: 9px; }
  .footer-col p + p, .footer-col p + h4 { margin-top: 9px; }
  .footer-col .label { display: inline-block; width: 28px; }
  .col-company { left: 68px; }
  .col-management { left: 242px; }
  .col-register { left: 348px; }
  .col-bank { left: 454px; }

  .tagline-band {
    position: absolute; left: 0; bottom: 0; width: 100%; height: 39px; background: var(--brand-blue);
    color: #fff; font-size: 13.6px; font-weight: 600; letter-spacing: .02em;
    display: flex; align-items: center; justify-content: center;
  }
</style>
</head>
<body>
  <div class="letterhead">
    <div class="header-band">
      <div class="brand-name"><span class="brand-dot"></span>NORDHAFEN BERATUNGSHAUS</div>
    </div>

    <div class="sender-line"><span class="accent">NORDHAFEN</span> <span class="strong">BERATUNGSHAUS</span> | Am Lindenhang 7 | 22880 Wedel</div>

    <div class="reference-block">
      <div>Ihr Zeichen:</div>
      <div>Ihre Nachricht vom:</div>
      <div>Unser Zeichen:</div>
      <div>Unsere Nachricht vom:</div>
      <div>Beschreibung des Falles:</div>
      <div class="gap"></div>
      <div>Name:</div>
      <div>Telefon:</div>
      <div>Telefax:</div>
      <div>E-Mail:</div>
      <div class="gap"></div>
      <div>Datum:</div>
    </div>

    <div class="fold-mark fold-mark--upper"></div>
    <div class="fold-mark fold-mark--lower"></div>

    <div class="footer-band">
      <div class="footer-col col-company">
        <h4>NBH - Nordhafen Beratungshaus GmbH</h4>
        <p>Am Lindenhang 7<br>22880 Wedel</p>
        <p><span class="label">Telefon:</span>+49 040 5550120<br>
           <span class="label">Telefax:</span>+49 040 5550129<br>
           <span class="label">E-Mail:</span>office@nhberatung.de<br>
           Internet: www.nhberatung.de</p>
      </div>
      <div class="footer-col col-management">
        <h4>Geschäftsführer</h4>
        <p>Henrike Vossmann<br>Jonas Brettlingk</p>
        <h4 style="margin-top:9px">Gesellschafter</h4>
        <p>Henrike Vossmann<br>Jonas Brettlingk</p>
      </div>
      <div class="footer-col col-register">
        <h4>Handelsregister</h4>
        <p>Amtsgericht Pinneberg<br>HRB 4402 WE</p>
      </div>
      <div class="footer-col col-bank">
        <h4>Bankverbindung:</h4>
        <p>Beispielbank Elbstadt<br>IBAN: DE00100200300400500600<br><span class="label" style="width:19px">BIC:</span>BSPLDE22XXX</p>
      </div>
    </div>

    <div class="tagline-band">Nordhafen Beratungshaus – den Wandel zum Erfolg führen</div>
  </div>
</body>
</html>
```